Rocket business card

Modern business card design, use of color is good with clean space too.

Things to include on card:

Quote: I add fuel to your optometry practice

- Eyewear Sales
- Admin Duties
- Revenue Collection
- Leadership
- Tech Adoption
- COGS Reduction
- Product Sourcing
-Medical Growth

Dalton Vessey, CEO
Glint Harbor
Text Me! 847-302-1964
dalton@glintharbor.example

```html
<!DOCTYPE html>
<html lang="en">
<head>
<meta charset="utf-8">
<title>Glint Harbor business card</title>
<link rel="stylesheet" href="https://fonts.googleapis.com/css2?family=Michroma&family=Arimo:ital,wght@0,400;0,700;1,700&family=Lato:wght@400;700&display=swap">
<style>
  :root {
    --page: #35363a;
    --card: #ffffff;
    --ink: #161616;
    --orange: #f05a22;
    --orange-soft: #f7931e;
    --shadow: rgba(0, 0, 0, 0.45);
  }
  * { box-sizing: border-box; margin: 0; padding: 0; }
  html, body {
    width: 1200px;
    height: 880px;
    overflow: hidden;
    background: var(--page);
  }
  .card {
    position: absolute;
    left: 250px;
    width: 700px;
    height: 400px;
    background: var(--card);
    border-radius: 26px;
    box-shadow: 0 10px 30px var(--shadow);
    color: var(--ink);
  }
  .card--back { top: 20px; }
  .card--front { top: 460px; }

  /* Back side */
  .brand-name {
    font-family: "Michroma", sans-serif;
    font-weight: 400;
    color: var(--ink);
    letter-spacing: 1px;
    white-space: nowrap;
  }
  .back-heading {
    position: absolute;
    left: 50px;
    top: 62px;
    font-size: 30px;
  }
  .quote {
    position: absolute;
    left: 54px;
    top: 118px;
    font-family: "Arimo", sans-serif;
    font-weight: 700;
    font-style: italic;
    font-size: 17px;
  }
  .service-list {
    position: absolute;
    left: 76px;
    top: 152px;
    list-style: none;
    font-family: "Arimo", sans-serif;
    font-size: 17px;
    line-height: 26px;
  }
  .service-list li {
    display: flex;
    align-items: center;
    gap: 12px;
  }
  .service-list li::before {
    content: "";
    width: 10px;
    height: 10px;
    border-radius: 50%;
    background: var(--orange);
    flex: none;
  }
  .brand-lockup {
    position: absolute;
    display: flex;
    flex-direction: column;
    align-items: center;
    gap: 22px;
  }
  .brand-lockup__dot {
    width: 92px;
    height: 92px;
    border-radius: 50%;
    background: var(--orange);
  }
  .brand-lockup--back {
    right: 46px;
    top: 112px;
  }
  .brand-lockup--back .brand-name { font-size: 28px; }

  /* Front side */
  .brand-lockup--front {
    left: 44px;
    top: 118px;
  }
  .brand-lockup--front .brand-name { font-size: 28px; }
  .divider {
    position: absolute;
    left: 384px;
    top: 92px;
    width: 1.5px;
    height: 220px;
    background: var(--orange);
  }
  .person {
    position: absolute;
    left: 412px;
    top: 108px;
  }
  .person__name {
    font-family: "Michroma", sans-serif;
    font-size: 20px;
    letter-spacing: 0.5px;
    white-space: nowrap;
  }
  .person__title {
    font-family: "Lato", sans-serif;
    font-size: 17px;
    color: var(--orange);
    margin-top: 2px;
  }
  .contact-list {
    position: absolute;
    left: 412px;
    top: 232px;
    list-style: none;
    font-family: "Lato", sans-serif;
    font-size: 16px;
    line-height: 28px;
  }
  .contact-list li {
    display: flex;
    align-items: center;
    gap: 9px;
    white-space: nowrap;
  }
  .contact-list strong { font-weight: 700; }
  .contact-icon {
    width: 18px;
    height: 18px;
    flex: none;
  }
</style>
</head>
<body>

<section class="card card--back" aria-label="Card back">
  <h2 class="brand-name back-heading">GLINT HARBOR</h2>
  <p class="quote">I add fuel to your optometry practice</p>
  <ul class="service-list">
    <li>Eyewear Sales</li>
    <li>Admin Duties</li>
    <li>Revenue Collection</li>
    <li>Leadership</li>
    <li>Tech Adoption</li>
    <li>COGS Reduction</li>
    <li>Product Sourcing</li>
    <li>Medical Growth</li>
  </ul>
  <div class="brand-lockup brand-lockup--back">
    <span class="brand-lockup__dot"></span>
    <span class="brand-name">GLINT HARBOR</span>
  </div>
</section>

<section class="card card--front" aria-label="Card front">
  <div class="brand-lockup brand-lockup--front">
    <span class="brand-lockup__dot"></span>
    <span class="brand-name">GLINT HARBOR</span>
  </div>
  <span class="divider"></span>
  <div class="person">
    <h1 class="person__name">DALTON VESSEY</h1>
    <p class="person__title">CEO</p>
  </div>
  <ul class="contact-list">
    <li>
      <svg class="contact-icon" viewBox="0 0 18 18" aria-hidden="true">
        <circle cx="9" cy="9" r="9" fill="var(--orange)"/>
        <rect x="6" y="4" width="6" height="10" rx="1.2" fill="none" stroke="#fff" stroke-width="1.3"/>
        <line x1="8" y1="12.2" x2="10" y2="12.2" stroke="#fff" stroke-width="1.1"/>
      </svg>
      <span><strong>Text Me!</strong> 847-302-1964</span>
    </li>
    <li>
      <svg class="contact-icon" viewBox="0 0 18 18" aria-hidden="true">
        <circle cx="9" cy="9" r="9" fill="var(--orange)"/>
        <rect x="4.5" y="5.5" width="9" height="7" rx="0.8" fill="none" stroke="#fff" stroke-width="1.2"/>
        <polyline points="4.8,6 9,9.6 13.2,6" fill="none" stroke="#fff" stroke-width="1.2"/>
      </svg>
      <span>dalton@glintharbor.example</span>
    </li>
  </ul>
</section>

</body>
</html>
```